Hair & Skin Product Line

I need someone to design clear product labels that can go on pink bottles. I'm looking for someone who can add graphics such as avocado and honey to the label as these are ingredients in our products. The colors we want incorporated are gold, blue, white and purple. I will upload information about our company identity and information on one label. Whoever we choose, we will use them to create 11 more labels.

Target Market(s)

Woman 25-50, Natural, straight or curly hair.

Industry/Entity Type

Beauty

```html
<!DOCTYPE html>
<html lang="en">
<head>
<meta charset="utf-8">
<title>Avocado &amp; Honey Moisture Repair Shampoo – Label</title>
<link rel="stylesheet" href="https://fonts.googleapis.com/css2?family=Montserrat:wght@400;500;600&family=Great+Vibes&display=swap">
<style>
  :root {
    --page-bg: #ffffff;
    --label-pink: #e8abca;
    --label-pink-deep: #de9bbd;
    --panel-white: #ffffff;
    --gold: #b88c4a;
    --gold-light: #cfa766;
    --honey-brown: #8a5a2b;
    --script-blue: #4d5fa3;
    --ink: #2c2226;
    --text-white: #ffffff;
    --art-green-light: #b9cf8a;
    --art-green: #8fae5c;
    --art-honey: #e7b24a;
  }
  html, body {
    margin: 0;
    padding: 0;
    width: 1200px;
    height: 1200px;
    overflow: hidden;
    background: var(--page-bg);
  }
  .canvas {
    position: relative;
    width: 1200px;
    height: 1200px;
  }
  .label {
    position: absolute;
    left: 314px;
    top: 60px;
    width: 572px;
    height: 1080px;
    background: linear-gradient(90deg, var(--label-pink-deep) 0%, var(--label-pink) 18%, var(--label-pink) 82%, var(--label-pink-deep) 100%);
    overflow: hidden;
    font-family: "Montserrat", sans-serif;
  }
  .brand-name {
    position: absolute;
    top: 160px;
    left: 0;
    width: 100%;
    text-align: center;
    font-family: "Great Vibes", cursive;
    font-size: 50px;
    color: var(--text-white);
    line-height: 1;
  }
  .ingredient-art {
    position: absolute;
    left: 0;
    top: 250px;
    width: 572px;
    height: 470px;
    background: linear-gradient(135deg, var(--art-green-light) 0%, var(--art-green) 55%, var(--art-honey) 100%);
    opacity: 0.85;
  }
  .title-panel {
    position: absolute;
    left: 136px;
    top: 310px;
    width: 330px;
    height: 370px;
    box-sizing: border-box;
    background: var(--panel-white);
    padding: 14px;
  }
  .title-frame {
    width: 100%;
    height: 100%;
    box-sizing: border-box;
    border: 2px solid var(--gold-light);
    padding: 54px 0 0 26px;
  }
  .title-line {
    margin: 0;
    line-height: 1.05;
    text-transform: uppercase;
  }
  .title-top {
    font-size: 31px;
    font-weight: 500;
    color: var(--gold);
    letter-spacing: 0.5px;
  }
  .title-main {
    font-size: 58px;
    font-weight: 600;
    color: var(--honey-brown);
    letter-spacing: 1px;
  }
  .title-sub {
    font-size: 26px;
    font-weight: 500;
    color: var(--gold);
  }
  .product-type {
    margin: 2px 0 0;
    font-family: "Great Vibes", cursive;
    font-size: 66px;
    line-height: 1;
    color: var(--script-blue);
  }
  .claims {
    position: absolute;
    top: 770px;
    left: 0;
    width: 100%;
    text-align: center;
  }
  .claims-infused {
    margin: 0 0 8px;
    font-size: 26px;
    font-weight: 600;
    color: var(--ink);
  }
  .claims-benefit {
    margin: 0;
    font-size: 24px;
    line-height: 1.3;
    color: var(--text-white);
  }
  .volume {
    position: absolute;
    top: 900px;
    left: 0;
    width: 100%;
    text-align: center;
    font-size: 28px;
    font-weight: 500;
    color: var(--ink);
    letter-spacing: 0.5px;
  }
</style>
</head>
<body>
<main class="canvas">
  <section class="label">
    <div class="ingredient-art" role="img" aria-label="Illustration of a whole avocado, a halved avocado with its pit, green leaves and a golden honey drip"></div>

    <div class="brand-name">Velvet Bloom</div>

    <div class="title-panel">
      <div class="title-frame">
        <p class="title-line title-top">Avocado &amp;</p>
        <p class="title-line title-main">Honey</p>
        <p class="title-line title-sub">Moisture Repair</p>
        <p class="product-type">shampoo</p>
      </div>
    </div>

    <div class="claims">
      <p class="claims-infused">Infused W/biotin + Rosemary</p>
      <p class="claims-benefit">Gently Cleanses and Hydrates<br>For Retention, Moisture And Softness</p>
    </div>

    <div class="volume">300 ML /10 FL OZ</div>
  </section>
</main>
</body>
</html>
```